Smart Home App Needs 4 Mockup Screens. Extra Work Guaranteed for Winner

BACKGROUND
Our company, Lumora, is launching an exciting new app early next year. And we need some examples of what our app will look like to show to some of the biggest retailers in the world. We hope that this project will lead to regular work as we have a lot of new products planned for the app.

Our app will support baby, home and pet monitors (cameras) as well as the world's first smart pet flap.

The monitors allow you to do much more than just watch live video. By monitoring and providing information on sound, movement and temperature the app provides the user with instant peace of mind wherever they are. If anything has changed the user can be alerted via notifications. If motion is detected the user will receive a clip of the whole event moments after it has happened.

The Smart Pet Flap is packed full of features too. From letting you decide when your pet can or can't go outside from your mobile, to automatically opening if a fire is detected (along with a whole host of other features) - this really is the most advanced pet flap in the world.

REQUIREMENTS
We need 4 mock-up screens creating to show the UI of our app.
1. Camera Home Page
2. Camera Notifications Page
3. Pet Flap Fire Alarm Warning Page
4. Extreme Weather Warning Page

Optional - Happy to Pay the Winner Extra for these Designs
5. Start Up/Log In Page
6. Pet Flap Notification Example
7. Pet Flap Scheduler Page (your choice)
(SEE LUMORA APP DESIGN COMPETITION - ATTACHED)

STYLE GUIDE
As you'll see from our wireframes we want our app to be very minimal and modern. The predominant colour will be white but where colour is used it should be bright (see our colour palette - which we will provide shortly).

INSPIRATION
We love the UI of Finchly (home surveillance). Also check out Vesk (smart thermostat).
(SEE LUMORA UI EXAMPLES ATTACHED)

LOGO
We love our logo. Feel free to use it in creative ways.

So far we're also using it as a kind of beacon to indicate if everything is ok.

LOGO COLOURS & APP COLOURS
As mentioned, we are thinking of using the green logo to indicate that everything is ok (and also for the pet app in general). We reserve red for when something has happened (normally bad) and needs attention, like a fire alarm going off.

The app will be predominantly black and white with the odd minimal flash of colour (probably primary colour)
We'll upload a colour scheme as soon as we have it.

CONTACT
Please message us for more details - we'll do our best to reply promptly.

FUTURE WORK
We will need extra screens made straight after the competition is over and there should be additional regular work after this.

Target Market(s)

Our app will be used by young professionals, to young parents to grandparents. The design must be contemporary but timeless and easy to use no matter how good you are with technology.

Industry/Entity Type

Pet

Font styles to use
Sans Serif

Colors
faee3f
33a6d7
ec1f27
acd036
32b7a4

Requirements
Must have
• Beautiful, minimal design. Make sure you spend time looking at the Finchly and Vesk apps before starting.

For the videos make sure you use sensible images - that you'd expect to see from a monitor (high resolution images if possible)
Nice to have
• Creative use of our logo.
Should not have
• Too much detail/clutter/colours. Ugly fonts.

```html
<!DOCTYPE html>
<html lang="en">
<head>
<meta charset="utf-8">
<title>Lumora PawPorta – Fire Alarm Warning</title>
<link rel="stylesheet" href="https://fonts.googleapis.com/css2?family=Varela+Round&family=Open+Sans:wght@400;600&display=swap">
<style>
  :root {
    --white: #ffffff;
    --ink: #2b2b2b;
    --ink-soft: #3a3a3a;
    --status-ink: #111111;
    --alert-red: #ec1f27;
    --safe-green: #54b848;
    --action-blue: #33a6d7;
    --flame-yellow: #faee3f;
    --muted-grey: #b9b9b9;
  }
  * { margin: 0; padding: 0; box-sizing: border-box; }
  html, body { width: 676px; height: 1200px; overflow: hidden; background: var(--white); }
  .screen {
    position: relative; width: 676px; height: 1200px;
    font-family: "Varela Round", sans-serif; color: var(--ink);
  }

  /* Status bar */
  .status-bar {
    position: absolute; top: 0; left: 0; width: 100%; height: 42px;
    font-family: "Open Sans", sans-serif; font-size: 21px; color: var(--status-ink);
  }
  .status-left { position: absolute; left: 10px; top: 8px; display: flex; align-items: center; gap: 6px; }
  .status-time { position: absolute; left: 0; right: 0; top: 7px; text-align: center; font-weight: 600; }
  .status-right { position: absolute; right: 10px; top: 8px; display: flex; align-items: center; gap: 6px; }

  /* Navigation */
  .nav-bar { position: absolute; top: 52px; left: 0; width: 100%; height: 56px; }
  .nav-back {
    position: absolute; left: 16px; top: 2px; display: flex; align-items: center; gap: 10px;
    font-family: "Open Sans", sans-serif; font-size: 39px; color: #555; font-weight: 400;
  }
  .nav-title {
    position: absolute; left: 0; right: 0; top: 2px; text-align: center;
    font-size: 39px; font-weight: 400; color: var(--action-blue);
  }

  /* Hero illustration area */
  .alert-illustration {
    position: absolute; left: 63px; top: 137px; width: 528px; height: 487px;
    background: radial-gradient(ellipse at 68% 70%, var(--flame-yellow) 0%, #f6a53a 22%, var(--alert-red) 48%, #f4f4f4 78%);
    border-radius: 8px;
  }
  .brand-mark {
    position: absolute; left: 122px; top: 556px; display: flex; align-items: center; gap: 8px;
    padding: 4px 12px; background: var(--white); border-radius: 18px;
    font-size: 22px; font-weight: 400; color: var(--alert-red);
  }
  .brand-dot { width: 16px; height: 16px; border-radius: 50%; background: var(--alert-red); }

  /* Message */
  .alert-heading {
    position: absolute; left: 0; right: 0; top: 648px; text-align: center;
    font-size: 40px; font-weight: 400; line-height: 50px; color: var(--ink);
  }
  .alert-detail {
    position: absolute; left: 0; right: 0; top: 697px; text-align: center;
    font-size: 30px; line-height: 38px; color: var(--ink-soft);
  }

  /* Actions */
  .action {
    position: absolute; left: 127px; display: flex; align-items: center; gap: 30px;
    font-size: 30px; line-height: 37px;
  }
  .action-icon { width: 52px; flex: 0 0 52px; display: flex; justify-content: center; }
  .action--keep-locked { top: 818px; color: var(--alert-red); }
  .action--let-in { top: 932px; color: var(--safe-green); }
  .action--call { top: 1062px; color: var(--action-blue); }

  .settings-button { position: absolute; right: 20px; bottom: 14px; }
</style>
</head>
<body>
<div class="screen">

  <header class="status-bar">
    <div class="status-left">
      <svg width="70" height="14" viewBox="0 0 70 14" aria-hidden="true">
        <circle cx="6" cy="7" r="5.5" fill="var(--status-ink)"/>
        <circle cx="20" cy="7" r="5.5" fill="var(--status-ink)"/>
        <circle cx="34" cy="7" r="5.5" fill="var(--status-ink)"/>
        <circle cx="48" cy="7" r="5.5" fill="var(--status-ink)"/>
        <circle cx="62" cy="7" r="5" fill="none" stroke="var(--status-ink)" stroke-width="1.2"/>
      </svg>
      <span>Telvo</span>
      <svg width="26" height="20" viewBox="0 0 26 20" aria-hidden="true">
        <path d="M13 19 L9 14.5 A6 6 0 0 1 17 14.5 Z" fill="var(--status-ink)"/>
        <path d="M5 10.5 A11.5 11.5 0 0 1 21 10.5" fill="none" stroke="var(--status-ink)" stroke-width="2.6"/>
        <path d="M1 6.5 A17 17 0 0 1 25 6.5" fill="none" stroke="var(--status-ink)" stroke-width="2.6"/>
      </svg>
    </div>
    <div class="status-time">7:41 PM</div>
    <div class="status-right">
      <svg width="20" height="20" viewBox="0 0 20 20" aria-hidden="true">
        <path d="M18 2 L2 9 L9 10.5 L10.5 18 Z" fill="var(--status-ink)"/>
      </svg>
      <span>55%</span>
      <svg width="50" height="22" viewBox="0 0 50 22" aria-hidden="true">
        <rect x="1" y="1" width="43" height="20" rx="3" fill="none" stroke="var(--status-ink)" stroke-width="1.6"/>
        <rect x="3.5" y="3.5" width="22" height="15" rx="1" fill="var(--status-ink)"/>
        <rect x="45" y="7" width="3.5" height="8" rx="1" fill="var(--status-ink)"/>
      </svg>
    </div>
  </header>

  <nav class="nav-bar">
    <div class="nav-back">
      <svg width="22" height="38" viewBox="0 0 22 38" aria-hidden="true">
        <path d="M19 3 L4 19 L19 35" fill="none" stroke="#555" stroke-width="3.5" stroke-linecap="round" stroke-linejoin="round"/>
      </svg>
      <span>Back</span>
    </div>
    <h1 class="nav-title">PawPorta</h1>
  </nav>

  <div class="alert-illustration" role="img" aria-label="Illustration of a house outline engulfed by large red and yellow flames"></div>
  <div class="brand-mark"><span class="brand-dot"></span><span>Lumora</span></div>

  <h2 class="alert-heading">Your fire alarm is is going off.</h2>
  <p class="alert-detail">Donnie has just gone outside so we’ve<br>locked him out as a percaution.</p>

  <div class="action action--keep-locked">
    <span class="action-icon">
      <svg width="48" height="60" viewBox="0 0 48 60" aria-hidden="true">
        <path d="M11 27 V17 A13 13 0 0 1 37 17 V27" fill="none" stroke="var(--alert-red)" stroke-width="2.4"/>
        <rect x="2" y="27" width="44" height="31" fill="none" stroke="var(--alert-red)" stroke-width="2.4"/>
      </svg>
    </span>
    <span>Keep Donnie locked<br>out until further notice.</span>
  </div>

  <div class="action action--let-in">
    <span class="action-icon">
      <svg width="48" height="62" viewBox="0 0 48 62" aria-hidden="true">
        <path d="M11 22 V16 A13 13 0 0 1 37 16 V20" fill="none" stroke="var(--safe-green)" stroke-width="2.4"/>
        <rect x="2" y="29" width="44" height="31" fill="none" stroke="var(--safe-green)" stroke-width="2.4"/>
      </svg>
    </span>
    <span>It is a false alarm;<br>let Donnie back in.</span>
  </div>

  <div class="action action--call">
    <span class="action-icon">
      <svg width="54" height="54" viewBox="0 0 54 54" aria-hidden="true">
        <path d="M12 3 C9 3 4 7 4 13 C4 30 24 50 41 50 C47 50 51 45 51 42 L43 34 C41 32 39 33 37 35 L34 38 C27 35 19 27 16 20 L19 17 C21 15 22 13 20 11 Z" fill="var(--action-blue)"/>
      </svg>
    </span>
    <span>Make a phone call.</span>
  </div>

  <div class="settings-button" aria-label="Settings">
    <svg width="44" height="44" viewBox="0 0 44 44" aria-hidden="true">
      <g fill="none" stroke="var(--muted-grey)" stroke-width="1.8" stroke-linejoin="round">
        <path d="M19 2 H25 L26 8 L30 10 L35 6 L39 10 L35 15 L37 19 L42 19 V25 L37 26 L35 30 L39 35 L35 39 L30 35 L26 37 L25 42 H19 L18 37 L14 35 L9 39 L5 35 L9 30 L7 26 L2 25 V19 L7 18 L9 14 L5 9 L9 5 L14 9 L18 7 Z"/>
        <circle cx="22" cy="22" r="7"/>
      </g>
    </svg>
  </div>

</div>
</body>
</html>
```